Business Card Design

Business card design and logo for new company called RMT Holdings, Inc.
No specific business product line so design would be more focused on the Company name and type style. I would like logo to incorporate Company Lettering "RMT" . Classic example of that would be the Lumo Broadcasting logo. Intent that the "RMT" lettering design would also be the Company Logo design.
Note that contact information for business card does not have telephone / fax numbers and web site as that will follow but make allowance for that information in the business card design. Several of the design layouts has small logo instead of the wording for phone, fax ..... which I would prefer.
Target Market(s)
Small Businesses
Industry/Entity Type
Business
Contact Information for Business Card
Dennis Pratt
RMT Holdings, Inc.
48620 Birch Hollow Lane, Unit F
Castaic, CA 91507
Phone: 555.218.6043
Mobile: 555.731.2964
FAX: 555.609.3178
Email: dpratt@rmtholdings.example
Web: www.rmtholdings.example
Font styles to use
Other font styles liked:
- Helvetica
Look and feel

```html
<!DOCTYPE html>
<html lang="en">
<head>
<meta charset="utf-8">
<title>RMT Holdings, Inc. — Business Card</title>
<link href="https://fonts.googleapis.com/css2?family=Open+Sans:wght@400;600&display=swap" rel="stylesheet">
<style>
  :root {
    --backdrop: #d9dadc;
    --card-dark: #121416;
    --card-mid: #24272a;
    --accent: #1ea6ec;
    --accent-soft: #138cd0;
    --text-light: #c9d2d8;
  }
  * { margin: 0; padding: 0; box-sizing: border-box; }
  html, body {
    width: 1200px; height: 988px; overflow: hidden;
    background: var(--backdrop);
    font-family: "Open Sans", Helvetica, Arial, sans-serif;
  }
  .canvas {
    width: 1200px; height: 988px;
    display: flex; flex-direction: column;
    align-items: center; justify-content: center; gap: 40px;
  }
  .card {
    position: relative;
    width: 760px; height: 434px;
    background: radial-gradient(ellipse at 55% 50%, var(--card-mid) 0%, var(--card-dark) 75%);
    overflow: hidden;
    box-shadow: 0 10px 26px rgba(0,0,0,.25);
  }
  .card__band {
    position: absolute; left: 0; right: 0; top: 0; height: 16px;
    background: var(--accent);
  }
  .card__rule {
    position: absolute; left: 0; right: 0; height: 3px;
    background: var(--accent);
  }
  .company-name {
    color: var(--accent); font-weight: 600; letter-spacing: .2px;
    white-space: nowrap;
  }
  /* Contact side */
  .card--contact .company-name {
    position: absolute; left: 44px; top: 74px; font-size: 38px;
  }
  .card--contact .rule-upper { top: 150px; }
  .card--contact .rule-lower { top: 322px; }
  .holder {
    position: absolute; left: 44px; top: 236px;
    color: var(--accent-soft); text-transform: uppercase;
    font-size: 15px; line-height: 1.5; letter-spacing: .6px;
  }
  .contact-list {
    position: absolute; left: 320px; top: 170px; width: 410px;
    display: grid; grid-template-columns: 1fr 1fr; row-gap: 12px; column-gap: 14px;
    list-style: none;
  }
  .contact-list li {
    display: flex; align-items: center; gap: 9px;
    color: var(--text-light); font-size: 13px; white-space: nowrap;
  }
  .contact-list li.wide { grid-column: 1 / 3; }
  .contact-icon { flex: 0 0 22px; width: 22px; height: 22px; }
  /* Name side */
  .card--front .company-name {
    position: absolute; left: 0; right: 0; top: 190px;
    text-align: center; font-size: 58px; padding-left: 70px;
  }
</style>
</head>
<body>
<main class="canvas">

  <section class="card card--contact" aria-label="Business card, contact side">
    <div class="card__band"></div>
    <h1 class="company-name">RMT Holdings, Inc.</h1>
    <div class="card__rule rule-upper"></div>

    <ul class="contact-list">
      <li>
        <svg class="contact-icon" viewBox="0 0 22 22" aria-hidden="true"><circle cx="11" cy="11" r="11" fill="#1ea6ec"/><path d="M7.5 6.2l2 .2.9 2.4-1.2 1a6 6 0 0 0 2.9 2.9l1-1.2 2.4.9.2 2c-.3.7-1 1-1.8.9A8.5 8.5 0 0 1 6.6 8c-.1-.8.2-1.5.9-1.8z" fill="#fff"/></svg>
        555.218.6043
      </li>
      <li>
        <svg class="contact-icon" viewBox="0 0 22 22" aria-hidden="true"><circle cx="11" cy="11" r="11" fill="#1ea6ec"/><rect x="7.5" y="5" width="7" height="12" rx="1.3" fill="#fff"/><rect x="8.6" y="6.6" width="4.8" height="7.4" fill="#1ea6ec"/><circle cx="11" cy="15.5" r=".7" fill="#1ea6ec"/></svg>
        555.731.2964
      </li>
      <li>
        <svg class="contact-icon" viewBox="0 0 22 22" aria-hidden="true"><circle cx="11" cy="11" r="11" fill="#1ea6ec"/><rect x="7.5" y="5.5" width="7" height="4" fill="#fff"/><rect x="5.5" y="9.5" width="11" height="5" rx="1" fill="#fff"/><rect x="7.5" y="13" width="7" height="3.5" fill="#fff" stroke="#1ea6ec" stroke-width=".8"/></svg>
        555.609.3178
      </li>
      <li>
        <svg class="contact-icon" viewBox="0 0 22 22" aria-hidden="true"><circle cx="11" cy="11" r="11" fill="#1ea6ec"/><circle cx="11" cy="11" r="5.5" fill="none" stroke="#fff" stroke-width="1.2"/><ellipse cx="11" cy="11" rx="2.4" ry="5.5" fill="none" stroke="#fff" stroke-width="1"/><path d="M5.5 11h11" stroke="#fff" stroke-width="1"/></svg>
        www.rmtholdings.example
      </li>
      <li class="wide">
        <svg class="contact-icon" viewBox="0 0 22 22" aria-hidden="true"><circle cx="11" cy="11" r="11" fill="#1ea6ec"/><rect x="5.5" y="7" width="11" height="8" rx="1" fill="#fff"/><path d="M5.8 7.4l5.2 4 5.2-4" fill="none" stroke="#1ea6ec" stroke-width="1.1"/></svg>
        dpratt@rmtholdings.example
      </li>
      <li class="wide">
        <svg class="contact-icon" viewBox="0 0 22 22" aria-hidden="true"><circle cx="11" cy="11" r="11" fill="#1ea6ec"/><path d="M11 17s-4.2-4.4-4.2-7.3a4.2 4.2 0 0 1 8.4 0C15.2 12.6 11 17 11 17z" fill="#fff"/><circle cx="11" cy="9.8" r="1.6" fill="#1ea6ec"/></svg>
        48620 Birch Hollow Lane, Unit F, Castaic, CA 91507
      </li>
    </ul>

    <p class="holder">Dennis Pratt<br>Financial Advisor</p>
    <div class="card__rule rule-lower"></div>
  </section>

  <section class="card card--front" aria-label="Business card, name side">
    <div class="card__band"></div>
    <h2 class="company-name">RMT Holdings, Inc.</h2>
  </section>

</main>
</body>
</html>
```